Bar and Grill looking or a Responsive Web design

New Bar and Grill in the Toronto area just opened up and is looking for a new wordpress website to start off his business.

Their business revolves around a homey family, upbeat atmosphere. His cuisine is gourmet pub style food. Speciality are home made burgers. 90 Seat restaurant in a very diverse and high density neighbourhood.

Looking for a responsive web design that will focus on a key feature pages.

Homepage
- Navigation is easy and simple, emphasize easy navigation in Mobile view.
- Contact information is a click or touch away

About Page

Menu Page
-Menu styling to be responsive. Very simple navigation through different menus and then menu would appear.

Gallery

Contact page
- Map (not googlesk)
- Contact Details
- Contact/Feedback form

They do have a logo and will be uploaded.

We are open to any designs, as well as designs based off templates that have already been created.

Target Market(s)

Target audience is the varied. They are in an area that's densely populated and very diverse. Looking for a crowd that appreciates a setting for sports, good gourmet pub styled food and a home styled restaurant.

Industry/Entity Type

Restaurant

Colors

Designer to choose colors to be used in the design.

Requirements
Must have
• Menus have to have responsive design for both mobile and tablet/desktop.
Nice to have
• Easy access contact button on mobile view. That way it will act like a webapp so that mobile devices can take advantage of quick touches to get in contact.

```html
<!DOCTYPE html>
<html lang="en">
<head>
<meta charset="utf-8">
<title>Maplecrest — Bar &amp; Grill</title>
<link rel="stylesheet" href="https://fonts.googleapis.com/css2?family=Bree+Serif&family=Bevan&family=Montserrat:wght@400&family=Open+Sans:wght@400;600&display=swap">
<style>
  :root{
    --brown-dark:#3f2216;
    --brown-deep:#5a2a16;
    --brown-tab:#7a3a1c;
    --wine:#7b2234;
    --cream:#ece8e2;
    --sand:#d7b69c;
    --sand-field:#ecd3bf;
    --gold:#e9b30f;
    --gold-light:#f6d24a;
    --text:#5b4a40;
    --heading:#2f2520;
    --footer-text:#d9c7b8;
    --white:#ffffff;
  }
  *{box-sizing:border-box;margin:0;padding:0}
  html,body{width:1137px;height:1200px;overflow:hidden}
  body{position:relative;background:var(--cream);font-family:"Montserrat",Arial,sans-serif;color:var(--text)}

  .hero{position:absolute;left:0;top:0;width:1137px;height:557px;
    background:radial-gradient(ellipse at 40% 20%,#e9c06a 0%,#b46b2c 30%,#6e3418 65%,#3a1a0c 100%)}
  .hero-topline{position:absolute;left:0;top:0;width:100%;height:7px;background:var(--brown-deep)}
  .hero-band{position:absolute;left:0;top:557px;width:100%;height:6px;background:#d1a98d}

  .brand{position:absolute;left:134px;top:7px;width:290px;height:141px;background:#f1ece2;
    border-radius:0 0 4px 4px;box-shadow:0 2px 6px rgba(0,0,0,.35);
    display:flex;align-items:center;justify-content:center;gap:10px;
    font-family:"Bree Serif",Georgia,serif;font-size:34px;color:#1f1a17}
  .brand-dot{width:14px;height:14px;border-radius:50%;background:#1f1a17}

  .nav{position:absolute;top:0;left:0;width:100%;height:97px}
  .nav a{position:absolute;top:50px;font-family:"Bree Serif",Georgia,serif;font-size:18px;color:var(--white);text-decoration:none}
  .nav .active-bg{position:absolute;left:486px;top:0;width:72px;height:97px;background:rgba(80,35,15,.55);border-bottom:2px solid #8a4a25}

  .hero-tagline{position:absolute;left:478px;top:434px;font-family:"Bevan",Georgia,serif;font-size:31px;line-height:48px;color:var(--wine);
    text-shadow:0 1px 1px rgba(255,235,210,.35)}

  .column-heading{position:absolute;font-family:"Bree Serif",Georgia,serif;font-weight:400;font-size:19px;color:var(--heading);top:597px}
  .photo{position:absolute;top:634px;width:274px;height:160px;border-bottom:4px solid #5a2a16}
  .column-text{position:absolute;top:810px;width:274px;font-size:12.8px;line-height:19.5px;color:var(--text)}
  .column-text a{color:#6a3418;text-decoration:none}

  .contact{position:absolute;left:730px;top:620px;width:273px;height:267px;background:var(--sand);border-radius:3px}
  .contact-tab{position:absolute;left:752px;top:599px;width:230px;height:40px;border-radius:10px;
    background:linear-gradient(#8b4520,#5e2a12);box-shadow:0 3px 0 #4a200d;
    font-family:"Bree Serif",Georgia,serif;font-size:19px;color:var(--white);display:flex;align-items:center;justify-content:center}
  .field{position:absolute;left:761px;width:212px;background:var(--sand-field);font-size:12px;color:#7a6658;padding:8px 8px}
  .subscribe{position:absolute;left:761px;top:842px;width:147px;height:30px;border-radius:15px;
    background:linear-gradient(var(--gold-light),var(--gold));border:1px solid #c99200;
    font-family:"Bree Serif",Georgia,serif;font-size:17px;color:#3d2a10;display:flex;align-items:center;justify-content:center}

  .footer-bg{position:absolute;left:0;top:935px;width:1137px;height:265px;background:var(--brown-dark)}
  .footer-heading{position:absolute;top:961px;font-family:"Open Sans",Arial,sans-serif;font-weight:400;font-size:19px;line-height:26px;color:var(--white)}
  .quick-links{position:absolute;left:133px;top:999px;list-style:none}
  .quick-links li{font-size:12.5px;line-height:19.5px;color:var(--footer-text)}
  .news-text{position:absolute;left:361px;top:999px;width:310px;font-size:12.5px;line-height:16px;color:var(--footer-text)}
  .news-input{position:absolute;left:362px;top:1053px;width:236px;height:33px;background:var(--white);font-size:12.5px;color:#555;padding:9px 8px}
  .news-send{position:absolute;left:598px;top:1053px;width:61px;height:33px;background:var(--gold);font-size:13px;color:#3d2a10;display:flex;align-items:center;justify-content:center}
  .hours{position:absolute;left:752px;top:996px;width:250px;border-collapse:collapse}
  .hours td{font-size:12.5px;color:var(--footer-text);height:26.5px;border-bottom:1px solid #54342a}
  .hours tr:last-child td{border-bottom:none}
  .hours td:last-child{text-align:right}
  .copyright{position:absolute;left:134px;top:1160px;font-size:12.5px;color:var(--footer-text)}
  .social{position:absolute;left:495px;top:1147px;display:flex;gap:9px}
  .social span{width:25px;height:25px;border-radius:50%;background:#c9b3a4}
</style>
</head>
<body>
  <header>
    <div class="hero" role="img" aria-label="Photo of a set restaurant table with wine glasses in warm evening light"></div>
    <div class="hero-topline"></div>
    <div class="hero-band"></div>
    <div class="brand"><span class="brand-dot"></span>Maplecrest</div>
    <nav class="nav">
      <div class="active-bg"></div>
      <a style="left:500px">Home</a>
      <a style="left:590px">About Us</a>
      <a style="left:707px">Menu</a>
      <a style="left:797px">Gallery</a>
      <a style="left:902px">Contact Us</a>
    </nav>
    <div class="hero-tagline">Unique &amp; Morden Restaurant<br>in the heart of your town.</div>
  </header>

  <main>
    <section>
      <h2 class="column-heading" style="left:133px">WELCOME TO MAPLECREST</h2>
      <div class="photo" style="left:133px;background:linear-gradient(120deg,#efe6dc,#b9a99a 60%,#6c5a4e)" role="img" aria-label="Photo of smiling restaurant staff and chefs in the kitchen"></div>
      <p class="column-text" style="left:133px">Lorem Ipsum is simply dummy text of the printing and typesetting industry. Lorem Ipsum has been the industry's standard dummy text ever 1500s....<a>[Read More]</a></p>
    </section>
    <section>
      <h2 class="column-heading" style="left:432px">OUR MENU</h2>
      <div class="photo" style="left:432px;background:linear-gradient(135deg,#6b8a3a,#d9482a 45%,#e8a23c 75%,#8a5a32)" role="img" aria-label="Photo of a homemade burger with fresh tomatoes and vegetables"></div>
      <p class="column-text" style="left:432px">Lorem Ipsum is simply dummy text of the printing and typesetting industry. Lorem Ipsum has been the industry's standard dummy text ever 1500s....<a>[Read More]</a></p>
    </section>
    <aside>
      <div class="contact"></div>
      <div class="contact-tab">CONTACT US</div>
      <div class="field" style="top:658px;height:29px">Your name</div>
      <div class="field" style="top:697px;height:28px">Your email</div>
      <div class="field" style="top:737px;height:91px">Message</div>
      <div class="subscribe">Subscribe Now</div>
    </aside>
  </main>

  <footer>
    <div class="footer-bg"></div>
    <h3 class="footer-heading" style="left:133px">Quick Links</h3>
    <ul class="quick-links">
      <li>Home</li><li>Documentation</li><li>Pricing</li><li>Support</li><li>Contact Us</li>
    </ul>
    <h3 class="footer-heading" style="left:359px">Newletter</h3>
    <p class="news-text">There are many variations of passages of lorem ipsum available.</p>
    <div class="news-input">Enter email</div>
    <div class="news-send">Send</div>
    <h3 class="footer-heading" style="left:752px">Our Hours</h3>
    <table class="hours">
      <tr><td>Monday</td><td>8:00 AM - 11:00 PM</td></tr>
      <tr><td>Tuesday</td><td>8:00 AM - 11:00 PM</td></tr>
      <tr><td>Wednesday</td><td>8:00 AM - 11:00 PM</td></tr>
      <tr><td>Thursday</td><td>8:00 AM - 11:00 PM</td></tr>
      <tr><td>Friday</td><td>8:00 AM - 11:00 PM</td></tr>
      <tr><td>Saturday</td><td>8:00 AM - 11:00 PM</td></tr>
      <tr><td>Sunday</td><td>Closed</td></tr>
    </table>
    <p class="copyright">copyright © 2013 Maplecrest. All rights reserved.</p>
    <div class="social" aria-label="Social links"><span></span><span></span><span></span><span></span><span></span></div>
  </footer>
</body>
</html>
```